Visitenkarten-Design für virtuelle Jobmesse & Jobbörse für Soldaten
Zielgruppe
Die KLO GmbH ist ein Unternehmen das zwei Hauptprodukte betreibt! Zum einen Jobbörse für Soldaten unter www.wachwechselpunkt.de und zum anderen eine virtuelle Jobmesse für Soldaten unter www.marvento.de , die wir zweimal im Jahr veranstalten.
Aufgabenstellung
Wir haben ja die beiden Produkte Wachwechselpunkt.de und die Marvento, für die bereits jeweils ein separtes Logo besteht! Diese finden Sie im Anhang! Beide werden doch jedoch von einem Unternehmen, der KLO GmbH betrieben! Aktuell nutzen wir eine Visitenkarte mit dem Logo von KLO und eine mit dem Logo der MARVENTO. Gerade im Hinblick darauf, dass wir zukünftig auch weiter Plattformen in unser Portfolio aufnehmen, möchte ich hier unsere V-Karten flexibler gestalten!
Ziel soll es also sein, eine Visitenkarte zu gestalten, auf dem klar wird, dass der Mitarbeiter von der KLO GmbH kommt, die KLO GmbH aber unterschiedliche Produkte betreibt.
Im Anhang finden Sie:
1. Das Logo von KLO
2. Das Logo von Marvento
3. Die aktuelle V-Karte von KLO
4. Die aktuelle V-Karte von MARVENTO
Vielleicht ein kleiner Anreiz: Aktuell nutzen wir auch zwei getrennte Geschäftspapiere. Das von www.wachwechselpunkt.de lade ich einmal hoch! Der Designer, der auch die Visitenkarte erstellt, erhällt im Anschluss den 1:1 Auftrag in Höhe von 200 Euro für die Erstellung des Geschäftspapiers! Wenn Sie jetzt schon einen Vorschlag für das Geschäftspapier einreichen, erhöht das natürlich Ihre Chancen, wobei ich verspreche, dass wir im Falle eine Annahme das 1:1 im Anschluß dennoch starten werden!

```html
<!DOCTYPE html>
<html lang="de">
<head>
<meta charset="utf-8">
<title>KLO GmbH – Visitenkarten</title>
<link href="https://fonts.googleapis.com/css2?family=Arimo:wght@400;700&display=swap" rel="stylesheet">
<style>
  :root{
    --stage:#c9b99c;
    --blue:#1c4a8a;
    --blue-soft:#8f98c8;
    --grey-line:#8a8a8a;
    --dark-card:#222222;
    --light-card:#f4f4f4;
    --text-dark:#333333;
    --text-muted:#555555;
    --white:#ffffff;
  }
  *{margin:0;padding:0;box-sizing:border-box}
  html,body{width:1200px;height:1200px;overflow:hidden;background:var(--stage)}
  body{font-family:"Arimo",Arial,sans-serif}
  .stage{position:absolute;left:0;top:0;width:985px;height:985px;transform:scale(1.21827);transform-origin:0 0}
  .card{position:absolute;width:335px;height:216px;overflow:hidden}
  .card--dark{background:var(--dark-card)}
  .card--light{background:var(--light-card)}
  .card--blue{background:var(--blue)}

  .front{left:148px}
  .back{left:501px}

  .top-rule{position:absolute;left:0;width:100%;height:2px}
  .top-rule--blue{top:8px;background:var(--blue)}
  .top-rule--grey{top:13px;background:var(--grey-line)}

  .brand{position:absolute;left:12px;top:94px;width:132px;text-align:center;font-size:12.5px;font-weight:700;color:var(--blue)}
  .card--dark .brand{color:#9aa9c8}
  .company{position:absolute;left:12px;top:131px;width:132px;text-align:center;font-size:13px;font-weight:700;color:var(--text-muted)}
  .card--dark .company{color:#4a4a4a}

  .divider{position:absolute;left:155px;top:50px;width:1px;height:113px;background:#777}

  .contact{position:absolute;left:174px;top:48px;width:155px;color:var(--text-dark)}
  .card--dark .contact{color:var(--text-muted)}
  .contact .name{font-size:17px;color:var(--blue);line-height:18px}
  .contact .role{font-size:9px;font-weight:700;letter-spacing:.4px;color:var(--text-muted);line-height:10px}
  .contact .address{margin-top:12px;font-size:11px;line-height:13px}
  .contact dl{margin-top:9px;display:grid;grid-template-columns:50px auto;row-gap:3px;font-size:11px;line-height:12px}
  .contact dt{color:var(--blue);font-size:10.5px}
  .contact .mail-row{margin-top:3px;font-size:9px;line-height:12px;letter-spacing:-.3px;white-space:nowrap}
  .contact .mail-row .label{color:var(--blue);font-size:10.5px;letter-spacing:0;margin-right:3px}

  .footer-band{position:absolute;left:0;bottom:0;width:335px;height:20px}
  .footer-band .url{position:absolute;right:12px;top:4px;font-size:11px;font-weight:700;color:var(--white)}

  .back-rule{position:absolute;left:0;width:100%;height:2px}
  .back-rule--blue{top:105px;background:var(--blue)}
  .back-rule--grey{top:111px;background:var(--grey-line)}
  .card--blue .back-rule--blue{background:var(--blue-soft)}
  .card--blue .back-rule--grey{background:#9a9a9a}
  .back-brand{position:absolute;left:50%;top:96px;transform:translateX(-50%);padding:0 10px;font-size:21px;font-weight:700;line-height:26px;white-space:nowrap}
  .card--dark .back-brand{background:var(--dark-card);color:var(--white)}
  .card--light .back-brand{background:var(--light-card);color:var(--blue)}
  .card--blue .back-brand{background:var(--blue);color:var(--white)}
</style>
</head>
<body>
<main class="stage">

  <svg width="0" height="0" style="position:absolute" aria-hidden="true">
    <defs>
      <linearGradient id="band-grey" x1="0" x2="1" y1="0" y2="0">
        <stop offset="0" stop-color="#9c9c9c"/>
        <stop offset=".45" stop-color="#4a4a4a"/>
        <stop offset=".75" stop-color="#cfcfcf"/>
        <stop offset="1" stop-color="#5a5a5a"/>
      </linearGradient>
      <symbol id="band" viewBox="0 0 335 20">
        <polygon points="0,0 132,0 124,20 0,20" fill="url(#band-grey)"/>
        <polygon points="138,0 143,0 135,20 130,20" fill="#6a6a6a"/>
        <polygon points="149,0 154,0 146,20 141,20" fill="#6a6a6a"/>
        <polygon points="160,0 335,0 335,20 152,20" fill="#1c4a8a"/>
      </symbol>
    </defs>
  </svg>

  <!-- Row 1: dark -->
  <section class="card card--dark front" style="top:122px">
    <div class="top-rule top-rule--blue"></div><div class="top-rule top-rule--grey"></div>
    <div class="brand">Wachwechselpunkt</div>
    <div class="company">KLO GmbH</div>
    <div class="divider"></div>
    <div class="contact">
      <div class="name">Jonas Berger</div>
      <div class="role">Geschäftsführer</div>
      <div class="address">Lindenweg 7<br>86444 Feldkirch</div>
      <dl>
        <dt>Telefon.:</dt><dd>08431 - 512 36 70</dd>
        <dt>Mobil.:</dt><dd>0176 - 318 52 904</dd>
      </dl>
      <div class="mail-row"><span class="label">E.:</span>j.berger@wachwechselpunkt.de</div>
    </div>
    <svg class="footer-band" viewBox="0 0 335 20"><use href="#band"/></svg>
    <div class="footer-band"><span class="url">www.wachwechselpunkt.de</span></div>
  </section>
  <section class="card card--dark back" style="top:124px">
    <div class="back-rule back-rule--blue"></div><div class="back-rule back-rule--grey"></div>
    <div class="back-brand">Wachwechselpunkt</div>
  </section>

  <!-- Row 2: light -->
  <section class="card card--light front" style="top:402px">
    <div class="top-rule top-rule--blue"></div><div class="top-rule top-rule--grey"></div>
    <div class="brand">Wachwechselpunkt</div>
    <div class="company">KLO GmbH</div>
    <div class="divider"></div>
    <div class="contact">
      <div class="name">Jonas Berger</div>
      <div class="role">Geschäftsführer</div>
      <div class="address">Lindenweg 7<br>86444 Feldkirch</div>
      <dl>
        <dt>Telefon.:</dt><dd>08431 - 512 36 70</dd>
        <dt>Mobil.:</dt><dd>0176 - 318 52 904</dd>
      </dl>
      <div class="mail-row"><span class="label">E.:</span>j.berger@wachwechselpunkt.de</div>
    </div>
    <svg class="footer-band" viewBox="0 0 335 20"><use href="#band"/></svg>
    <div class="footer-band"><span class="url">www.wachwechselpunkt.de</span></div>
  </section>
  <section class="card card--light back" style="top:404px">
    <div class="back-rule back-rule--blue"></div><div class="back-rule back-rule--grey"></div>
    <div class="back-brand">Wachwechselpunkt</div>
  </section>

  <!-- Row 3: light front, blue back -->
  <section class="card card--light front" style="top:685px">
    <div class="top-rule top-rule--blue"></div><div class="top-rule top-rule--grey"></div>
    <div class="brand">Wachwechselpunkt</div>
    <div class="company">KLO GmbH</div>
    <div class="divider"></div>
    <div class="contact">
      <div class="name">Jonas Berger</div>
      <div class="role">Geschäftsführer</div>
      <div class="address">Lindenweg 7<br>86444 Feldkirch</div>
      <dl>
        <dt>Telefon.:</dt><dd>08431 - 512 36 70</dd>
        <dt>Mobil.:</dt><dd>0176 - 318 52 904</dd>
      </dl>
      <div class="mail-row"><span class="label">E.:</span>j.berger@wachwechselpunkt.de</div>
    </div>
    <svg class="footer-band" viewBox="0 0 335 20"><use href="#band"/></svg>
    <div class="footer-band"><span class="url">www.wachwechselpunkt.de</span></div>
  </section>
  <section class="card card--blue back" style="top:688px">
    <div class="back-rule back-rule--blue"></div><div class="back-rule back-rule--grey"></div>
    <div class="back-brand">Wachwechselpunkt</div>
  </section>

</main>
</body>
</html>
```